Modern Business Card For A Digital Advertising Company

I'll be print on the Tarn Prints Velour paper http://us.tarnprints.example/products/velour/business-cards.html
Need's to be modern and use the color palette of the logo or gray scales. I think integrating the pixelation of the logo in to the card and having it wrap from one side to the other could be interesting. My company provides ad operations, web development, and number of other services to websites around the world. You can see my website at http://www.pixelharbor.example
Contact info on the card needs to have
Dana Welloby
President
p.555.318.4406
dana@pixelharbor.example
http://www.pixelharbor.example
Doesn't necessarily need to be in that order
Target Market(s)
Website owners
Industry/Entity Type
Business
Look and feel

```html
<!DOCTYPE html>
<html lang="en">
<head>
<meta charset="utf-8">
<title>Pixel Harbor – Business Card</title>
<link rel="stylesheet" href="https://fonts.googleapis.com/css2?family=Raleway:wght@200;300;600&display=swap">
<style>
  :root {
    --backdrop: #d9d6d1;
    --card-light: #5d605e;
    --card-dark: #2c2e2d;
    --logo-side: #0b0b0b;
    --accent: #8ee23a;
    --name-ink: #c9cccb;
    --title-ink: #8d918f;
    --contact-ink: #c2c5c4;
  }
  * { box-sizing: border-box; margin: 0; padding: 0; }
  html, body { width: 1200px; height: 741px; overflow: hidden; }
  body {
    background: var(--backdrop);
    font-family: "Raleway", sans-serif;
    display: flex;
    align-items: center;
    justify-content: center;
    gap: 40px;
  }
  .card {
    width: 525px;
    height: 300px;
    border-radius: 3px;
    position: relative;
    overflow: hidden;
    box-shadow: 0 10px 24px rgba(0,0,0,.25);
  }
  .card--contact {
    background: linear-gradient(135deg, var(--card-light) 0%, #434644 45%, var(--card-dark) 100%);
  }
  .contact__name {
    position: absolute;
    left: 44px;
    top: 52px;
    color: var(--name-ink);
    font-weight: 200;
    font-size: 40px;
    letter-spacing: 1px;
  }
  .contact__title {
    position: absolute;
    left: 150px;
    top: 104px;
    color: var(--title-ink);
    font-weight: 300;
    font-size: 15px;
    letter-spacing: 7px;
  }
  .contact__list {
    position: absolute;
    left: 44px;
    bottom: 38px;
    list-style: none;
    display: flex;
    flex-direction: column;
    gap: 9px;
  }
  .contact__item {
    display: flex;
    align-items: center;
    gap: 10px;
    color: var(--contact-ink);
    font-weight: 300;
    font-size: 14px;
    letter-spacing: .4px;
  }
  .contact__item--phone { font-size: 17px; letter-spacing: 1px; }
  .contact__icon { width: 13px; height: 13px; flex: none; }
  .card--brand {
    background: var(--logo-side);
    display: flex;
    align-items: center;
    justify-content: center;
    gap: 16px;
  }
  .brand__mark {
    width: 34px;
    height: 34px;
    background: var(--accent);
  }
  .brand__name {
    color: var(--accent);
    font-weight: 600;
    font-size: 50px;
    letter-spacing: 1px;
  }
</style>
</head>
<body>
  <section class="card card--contact">
    <h1 class="contact__name">Dana Welloby</h1>
    <p class="contact__title">President</p>
    <ul class="contact__list">
      <li class="contact__item contact__item--phone">
        <svg class="contact__icon" viewBox="0 0 13 13" aria-hidden="true">
          <rect x="3.5" y="0.5" width="6" height="12" rx="1.2" fill="none" stroke="#8ee23a" stroke-width="1.2"/>
          <circle cx="6.5" cy="10.4" r="0.8" fill="#8ee23a"/>
        </svg>
        555 - 318 - 4406
      </li>
      <li class="contact__item">
        <svg class="contact__icon" viewBox="0 0 13 13" aria-hidden="true">
          <rect x="0.6" y="2.6" width="11.8" height="8" fill="none" stroke="#8ee23a" stroke-width="1.2"/>
          <path d="M0.6 2.8 6.5 7.4 12.4 2.8" fill="none" stroke="#8ee23a" stroke-width="1.2"/>
        </svg>
        dana@pixelharbor.example
      </li>
      <li class="contact__item">
        <svg class="contact__icon" viewBox="0 0 13 13" aria-hidden="true">
          <circle cx="6.5" cy="6.5" r="5.8" fill="none" stroke="#8ee23a" stroke-width="1.2"/>
          <ellipse cx="6.5" cy="6.5" rx="2.4" ry="5.8" fill="none" stroke="#8ee23a" stroke-width="1"/>
          <path d="M0.8 6.5h11.4" stroke="#8ee23a" stroke-width="1"/>
        </svg>
        http://www.pixelharbor.example
      </li>
    </ul>
  </section>

  <section class="card card--brand">
    <span class="brand__mark" aria-hidden="true"></span>
    <p class="brand__name">Pixel Harbor</p>
  </section>
</body>
</html>
```